Whole Body Cryotherapy Business needs a Brochure

We need a brochure for marketing events of our spa. The name of the business is FrostHaven. Our website is www.frosthavenspa-example.com. We are located in New York City at the Lindenmark. We need an eye catching brochure that discusses the health benefits of whole body cryotherapy. We need an editable file to be able to tweak the language of the brochure. The contact information that should be on the brochure is as follows:

FrostHaven
Lindenmark, 482 W. 19th Street
New York, NY 10388

Phone: (855) 614-3098

EMail: frosthavenspa@mailbox-example.com

We prefer a color scheme that mainly uses blue, but are open to any design that is eye catching.

We need the brochure to fit on 8.5" x 11" paper.

Requirements
Must have
• Must have space for the following paragraphs (use Lorem Ipsem and we can fill in later): (1) What is Whole Body Cryotherapy and (2) What makes FrostHaven different.

```html
<!DOCTYPE html>
<html lang="en">
<head>
<meta charset="utf-8">
<title>FrostHaven Whole Body Cryotherapy Brochure</title>
<link href="https://fonts.googleapis.com/css2?family=PT+Sans:wght@400;700&family=Fira+Sans+Condensed:wght@300;400;600;700&display=swap" rel="stylesheet">
<style>
  :root{
    --stage:#ffffff;
    --hero-grey:#b6b9c6;
    --hero-grey-light:#cdd0da;
    --white:#ffffff;
    --ink:#1c1c1c;
    --band-red:#e8413a;
    --accent-red:#e8413a;
    --heading-blue:#17509e;
    --ice-top:#f6fbfe;
    --ice-bottom:#a9d9f3;
    --photo-deep:#1d2a6b;
    --photo-mist:#8aa6e0;
    --photo-steel:#8e9299;
    --photo-fog:#dfe9f0;
  }
  *{box-sizing:border-box;margin:0;padding:0}
  html,body{width:1001px;height:1200px;overflow:hidden;background:var(--stage)}
  .stage{position:relative;width:1001px;height:1200px}
  .brochure{
    position:absolute;left:41px;top:5px;width:983px;height:1273px;
    transform:scale(0.935);transform-origin:top left;
    font-family:"PT Sans",sans-serif;color:var(--ink);overflow:hidden;
  }
  .hero{
    position:absolute;left:0;top:0;width:983px;height:607px;
    background:radial-gradient(circle at 80% 25%,var(--hero-grey-light),var(--hero-grey) 70%);
  }
  .hero-photo{
    position:absolute;left:70px;top:20px;width:380px;height:462px;
    background:radial-gradient(ellipse at 45% 70%,var(--photo-mist),var(--photo-deep) 75%);
    border-radius:6px 6px 40px 40px;
  }
  .hero-tagline{
    position:absolute;left:40px;top:500px;width:400px;text-align:center;
    font-family:"Fira Sans Condensed",sans-serif;font-weight:300;font-size:31px;line-height:45px;color:var(--ink);
  }
  .brand-ring{position:absolute;left:640px;top:55px}
  .brand-name{
    position:absolute;left:508px;top:180px;width:400px;text-align:center;
    font-family:"PT Sans",sans-serif;font-weight:700;font-size:60px;color:var(--white);
  }
  .headline{
    position:absolute;left:480px;top:298px;width:455px;text-align:center;
    font-family:"Fira Sans Condensed",sans-serif;font-weight:700;font-size:70px;line-height:82px;
    color:var(--white);text-shadow:2px 3px 4px rgba(0,0,0,.35);
  }
  .address{
    position:absolute;left:480px;top:496px;width:455px;text-align:center;
    font-size:19px;line-height:26px;
  }
  .address strong{font-weight:700}
  .email{
    position:absolute;left:470px;top:553px;width:475px;text-align:center;
    font-size:25px;letter-spacing:1px;
  }
  .contact-band{
    position:absolute;left:0;top:607px;width:983px;height:56px;background:var(--band-red);color:var(--white);
  }
  .contact-band .web{
    position:absolute;left:48px;top:10px;font-weight:700;font-size:27px;letter-spacing:1.5px;
  }
  .contact-band .phone{
    position:absolute;left:493px;top:4px;font-family:"Fira Sans Condensed",sans-serif;font-weight:300;font-size:33px;
  }
  .contact-band .phone b{font-weight:700;font-size:39px}
  .info{
    position:absolute;left:0;top:663px;width:983px;height:610px;
    background:linear-gradient(160deg,var(--ice-top) 0%,#d4ecf9 40%,var(--ice-bottom) 100%);
  }
  h2{
    font-family:"PT Sans",sans-serif;font-weight:700;font-size:27px;line-height:32px;color:var(--heading-blue);
  }
  .col-left{position:absolute;left:48px;top:23px;width:406px}
  .col-left p{margin-top:14px;font-size:16px;line-height:20px;text-align:justify;word-spacing:1px}
  .col-left h2.benefits-title{margin-top:38px}
  .benefits{list-style:none;margin-top:14px}
  .benefits li{position:relative;padding-left:24px;font-size:15.5px;line-height:23px}
  .benefits li::before{
    content:"";position:absolute;left:0;top:7px;width:11px;height:11px;border-radius:50%;background:var(--accent-red);
  }
  .col-right{position:absolute;left:495px;top:23px;width:438px}
  .col-right p{margin-top:14px;font-size:16px;line-height:20.8px;text-align:justify;word-spacing:1px}
  .wrap-spacer{float:right;width:0;height:125px}
  .wrap-gap{float:right;clear:right;width:195px;height:80px}
  .side-photo{
    position:absolute;left:758px;top:199px;width:225px;height:411px;
    background:linear-gradient(90deg,var(--photo-steel),var(--photo-fog) 45%,var(--photo-steel));
    border-radius:60px 10px 0 0;
  }
  .promo{
    position:absolute;left:485px;top:292px;width:240px;text-align:center;
    font-weight:700;font-size:27px;line-height:35px;color:var(--accent-red);
  }
  .offer-ring{position:absolute;left:541px;top:412px}
  .offer{
    position:absolute;left:465px;top:542px;width:280px;text-align:center;
    font-family:"Fira Sans Condensed",sans-serif;font-weight:300;font-size:28px;
  }
</style>
</head>
<body>
<div class="stage">
  <article class="brochure">
    <header class="hero">
      <div class="hero-photo" role="img" aria-label="Photo of a whole body cryotherapy chamber glowing blue with cold mist"></div>
      <p class="hero-tagline">Wholebody Cryotherapy<br>is coming to NYC</p>
      <svg class="brand-ring" width="120" height="120" viewBox="0 0 120 120" aria-hidden="true">
        <circle cx="60" cy="60" r="56" fill="none" stroke="var(--white)" stroke-width="5"/>
      </svg>
      <div class="brand-name">FrostHaven</div>
      <h1 class="headline">FREEZE INTO<br>FITNESS</h1>
      <p class="address"><strong>FrostHaven,</strong> Lindenmark, 482 W. 19th Street<br>New York, NY 10388</p>
      <p class="email">frosthavenspa@mailbox-example.com</p>
    </header>

    <div class="contact-band">
      <span class="web">www.frosthavenspa-example.com</span>
      <span class="phone">Contact us : <b>(855) 614-3098</b></span>
    </div>

    <section class="info">
      <div class="col-left">
        <h2>What is Whole Body<br>Cryotherapy</h2>
        <p>Lorem ipsum dolor sit amet, consectetur adipiscing elit, sed do eiusmod tempor incididunt ut labore et dolore magna aliqua. Ut enim ad minim veniam, quis nostrud exercitation ullamco laboris nisi ut aliquip ex ea commodo consequat. Duis aute irure dolor in reprehenderit in voluptate velit esse cillum dolore eu fugiat nulla pariatur. Excepteur sint occaecat cupidatat non proident, sunt in culpa qui officia deserunt mollit anim id est laborum</p>
        <h2 class="benefits-title">Health benefits of whole body<br>cryotherapy</h2>
        <ul class="benefits">
          <li>Lorem ipsum dolor sit amet, consectetur sit</li>
          <li>Lorem ipsum dolor sit amet, consectetur dolor amet</li>
          <li>Lorem ipsum dolor sit amet, consectetur dolor sit</li>
          <li>Lorem ipsum dolor sit amet, consectetur sit amet</li>
          <li>Lorem ipsum dolor sit amet, consectetur sit amet</li>
          <li>Lorem ipsum dolor sit amet, consectetur dolor sit</li>
          <li>Lorem ipsum dolor sit amet, consectetur sit amet</li>
          <li>Lorem ipsum dolor sit consectetur dolor sit amet</li>
        </ul>
      </div>

      <div class="col-right">
        <h2>What makes FrostHaven different</h2>
        <p><span class="wrap-spacer"></span><span class="wrap-gap"></span>Lorem ipsum dolor sit amet, consectetur adipiscing elit, sed do eiusmod tempor incididunt ut labore et dolore magna aliqua. Ut enim ad minim veniam, quis nostrud exercitation ullamco laboris nisi ut aliquip ex ea commodo consequat. Duis aute irure dolor in reprehenderit in voluptate velit esse cillum dolore eu fugiat nulla pariatur. Excepteur sint occaecat cupidatat non proident, sunt in culpa qui officia deserunt mollit anim id est laborum.</p>
      </div>

      <div class="side-photo" role="img" aria-label="Photo of a client stepping out of a steel cryotherapy cabin surrounded by cold vapour"></div>
      <p class="promo">Lorem ipsum<br>dolor sit amet<br>consectetur</p>
      <svg class="offer-ring" width="120" height="120" viewBox="0 0 120 120" aria-hidden="true">
        <circle cx="60" cy="60" r="56" fill="none" stroke="var(--white)" stroke-width="5"/>
      </svg>
      <p class="offer">Claim your free session</p>
    </section>
  </article>
</div>
</body>
</html>
```